Iron Pivot Hoops Academy- Small Group and Private Lessons

I would like to advertise and drive my small group basketball lessons (offered on Fridays during the summer in Prosper, Texas with the following four groups- 1. Middle School Girls Small Group, 2. Middle School Boys Small Group, 3. High School Girls Small Group, 4. High School Boys Small Group).
Tag Line- "Do you want to become a complete player?"
We work to make each player as well rounded as possible by focusing on: balanced footwork, ballhandling, dribbling, finishing, passing, shooting, moving without the ball, basketball IQ
Website- www.ironpivothoopsacademy.com

```html
<!DOCTYPE html>
<html lang="en">
<head>
<meta charset="utf-8">
<title>Iron Pivot Hoops Academy – Small Group Lessons</title>
<link href="https://fonts.googleapis.com/css2?family=Oswald:wght@400;500;600;700&display=swap" rel="stylesheet">
<style>
  :root {
    --stage: #e0d9d4;
    --charcoal: #3a3a3c;
    --charcoal-deep: #2b2b2d;
    --orange: #f07d22;
    --white: #ffffff;
    --ink: #3d3d3f;
    --band: rgba(255, 255, 255, 0.72);
    --panel: rgba(40, 28, 24, 0.78);
    --gym-light: #e9d3b8;
    --gym-mid: #c99a6e;
    --gym-floor: #b77a43;
    --gym-dark: #6e3f1f;
  }
  * { margin: 0; padding: 0; box-sizing: border-box; }
  html, body {
    width: 1200px;
    height: 586px;
    overflow: hidden;
    background: var(--stage);
    font-family: "Oswald", sans-serif;
  }
  .flyer {
    position: absolute;
    left: 393px;
    top: 0;
    width: 414px;
    height: 586px;
    background: var(--white);
    overflow: hidden;
  }
  .brand {
    position: absolute;
    left: 14px;
    top: 22px;
    width: 112px;
    height: 70px;
    display: flex;
    align-items: center;
    gap: 6px;
  }
  .brand-dot {
    flex: 0 0 18px;
    height: 18px;
    border-radius: 50%;
    background: var(--orange);
  }
  .brand-name {
    font-weight: 600;
    font-size: 13px;
    line-height: 1.15;
    color: var(--charcoal);
    text-transform: uppercase;
  }
  .gym-photo {
    position: absolute;
    left: 0;
    top: 112px;
    width: 414px;
    height: 444px;
    background:
      radial-gradient(ellipse 150px 120px at 136px 318px, #c7692e 0%, #a5521f 55%, rgba(165,82,31,0) 100%),
      linear-gradient(180deg, var(--gym-light) 0%, #dcc0a0 30%, var(--gym-mid) 52%, var(--gym-floor) 70%, var(--gym-dark) 100%);
  }
  .headline {
    position: absolute;
    left: 138px;
    top: 0;
    width: 262px;
    height: 141px;
    background: var(--charcoal);
    border: 3px solid var(--orange);
    border-top: none;
    border-radius: 0 0 12px 12px;
    text-align: center;
    color: var(--white);
    font-weight: 700;
    text-transform: uppercase;
    padding-top: 17px;
  }
  .headline .line { display: block; font-size: 28px; line-height: 1.05; }
  .headline .accent { display: block; font-size: 40px; line-height: 1.1; color: var(--orange); }
  .groups {
    position: absolute;
    left: 0;
    top: 152px;
    width: 414px;
    height: 132px;
    background: var(--band);
    padding: 8px 12px;
    color: var(--ink);
    text-transform: uppercase;
  }
  .groups-intro { font-size: 13px; font-weight: 500; line-height: 1.2; }
  .groups-list { list-style: none; margin-top: 4px; }
  .groups-list li { font-size: 16px; font-weight: 500; line-height: 1.33; }
  .groups-list .num { color: var(--orange); }
  .focus {
    position: absolute;
    left: 274px;
    top: 306px;
    width: 128px;
    height: 184px;
    background: var(--panel);
    color: var(--white);
    text-align: center;
    text-transform: uppercase;
    font-size: 11px;
    font-weight: 500;
    line-height: 1.3;
    padding: 14px 6px;
  }
  .focus p + p { margin-top: 10px; }
  .contact {
    position: absolute;
    left: 0;
    top: 556px;
    width: 414px;
    height: 30px;
    background: var(--charcoal-deep);
    color: var(--white);
    font-size: 9px;
    display: flex;
    align-items: center;
    padding-left: 18px;
    gap: 9px;
  }
  .contact .sep { color: var(--orange); }
</style>
</head>
<body>
  <main class="flyer">
    <div class="gym-photo" role="img" aria-label="Basketball resting on a gym hardwood floor with blurred bleachers behind"></div>

    <div class="brand">
      <span class="brand-dot"></span>
      <span class="brand-name">Iron Pivot Hoops Academy</span>
    </div>

    <h1 class="headline">
      <span class="line">Do you want to</span>
      <span class="line">become a complete</span>
      <span class="accent">Player?</span>
    </h1>

    <section class="groups">
      <p class="groups-intro">Offered on Fridays during the summer in Prosper, Texas with the following four groups</p>
      <ol class="groups-list">
        <li><span class="num">1.</span> Middle School Girls Small Group,</li>
        <li><span class="num">2.</span> Middle School Boys Small Group,</li>
        <li><span class="num">3.</span> High School Girls Small Group,</li>
        <li><span class="num">4.</span> High School Boys Small Group</li>
      </ol>
    </section>

    <aside class="focus">
      <p>We work to make each player as well rounded as possible by focusing on:</p>
      <p>Balanced footwork, ballhandling, dribbling, finishing, passing, shooting, moving without the ball, basketball IQ</p>
    </aside>

    <footer class="contact">
      <span>555-014-2270</span>
      <span class="sep">|</span>
      <span>info@ironpivothoops.com</span>
      <span class="sep">|</span>
      <span>www.ironpivothoopsacademy.com</span>
    </footer>
  </main>
</body>
</html>
```